TRU PEAK POWER.

I'd like my business logo.
contact name: Desmond Halvik
phone:0438275160
email: info@trupeakpower.net.au
website: www.trupeakpower.net.au

services:
solar
battery storage
LED lighting
energy saving solutions
general electrical
I'd like the design to look professional

Target Market(s)

Everyone

Industry/Entity Type

Business

Contact Information for Business Card

as described above

Requirements
Must have
• Id like the colours and the design to work well with my logo.

```html
<!DOCTYPE html>
<html lang="en">
<head>
<meta charset="utf-8">
<title>Tru Peak Power – Business Card</title>
<link rel="stylesheet" href="https://fonts.googleapis.com/css2?family=Open+Sans:wght@400;600;700&family=Varela+Round&display=swap">
<style>
  :root {
    --bg: #bfe3d8;
    --card: #ffffff;
    --green-dark: #23935f;
    --green: #3fae76;
    --green-light: #4dbb84;
    --brand-green: #3aa85a;
    --orange: #f7a823;
    --orange-dark: #ef8a1f;
    --name-orange: #e0771f;
    --ink: #1e1e1e;
  }
  * { margin: 0; padding: 0; box-sizing: border-box; }
  html, body { width: 1200px; height: 1200px; overflow: hidden; }
  body {
    background: var(--bg);
    font-family: "Open Sans", Arial, sans-serif;
    color: var(--ink);
    position: relative;
  }
  .business-card {
    position: absolute;
    left: 100px; top: 300px;
    width: 1000px; height: 600px;
    background: var(--card);
    border-radius: 44px;
    overflow: hidden;
    box-shadow: 0 14px 34px rgba(0,0,0,0.12);
  }
  .band-left {
    position: absolute; left: 0; top: 0;
    width: 78px; height: 100%;
    background: linear-gradient(180deg, var(--green-light), var(--green-dark));
  }
  .band-right {
    position: absolute; right: 0; top: 0;
    width: 62px; height: 100%;
    background: var(--orange);
    border-left: 14px solid var(--orange-dark);
  }
  .icon-strip {
    position: absolute; left: 0;
    width: 78px; height: 38px;
    display: flex; align-items: center; justify-content: center;
    border-top: 1px solid rgba(255,255,255,0.25);
    background: rgba(255,255,255,0.08);
  }
  .icon-strip svg { width: 26px; height: 26px; }
  .brand {
    position: absolute; left: 78px; right: 62px; top: 110px;
    display: flex; align-items: center; justify-content: center; gap: 22px;
  }
  .brand-dot {
    width: 64px; height: 64px; border-radius: 50%;
    background: var(--orange);
  }
  .brand-name {
    font-weight: 700; font-size: 62px; letter-spacing: 1px;
    color: var(--brand-green);
  }
  .services {
    position: absolute; left: 78px; right: 62px; top: 212px;
    text-align: center; font-size: 24px; line-height: 1.35;
  }
  .contact-name {
    position: absolute; right: 110px; top: 318px;
    font-family: "Varela Round", "Open Sans", sans-serif;
    font-size: 52px; color: var(--name-orange); font-weight: 400;
    -webkit-text-stroke: 1.2px var(--name-orange);
  }
  .licence {
    position: absolute; right: 100px; top: 408px;
    font-size: 27px;
  }
  .contact-list {
    position: absolute; left: 108px; top: 446px;
    list-style: none; font-size: 29px; line-height: 42px;
  }
</style>
</head>
<body>
  <section class="business-card">
    <div class="band-left"></div>
    <div class="band-right"></div>

    <div class="icon-strip" style="top:446px">
      <svg viewBox="0 0 24 24" aria-hidden="true"><path fill="#fff" d="M6.6 10.8a15 15 0 0 0 6.6 6.6l2.2-2.2a1 1 0 0 1 1-.25 11.4 11.4 0 0 0 3.6.57 1 1 0 0 1 1 1V20a1 1 0 0 1-1 1A17 17 0 0 1 3 4a1 1 0 0 1 1-1h3.5a1 1 0 0 1 1 1c0 1.25.2 2.45.57 3.57a1 1 0 0 1-.25 1z"/></svg>
    </div>
    <div class="icon-strip" style="top:488px">
      <svg viewBox="0 0 24 24" aria-hidden="true"><rect x="2" y="5" width="20" height="14" rx="1" fill="#fff"/><path d="M2 6l10 7 10-7" fill="none" stroke="#2f9f6a" stroke-width="1.6"/></svg>
    </div>
    <div class="icon-strip" style="top:530px">
      <svg viewBox="0 0 24 24" aria-hidden="true" fill="none" stroke="#fff" stroke-width="1.4"><circle cx="12" cy="12" r="9"/><ellipse cx="12" cy="12" rx="4" ry="9"/><path d="M3 12h18M5 7h14M5 17h14"/></svg>
    </div>

    <header class="brand">
      <span class="brand-dot"></span>
      <span class="brand-name">TRU PEAK POWER</span>
    </header>

    <p class="services">Solar, Battery storage, LED lighting,<br>Energy saving solutions, General electrical</p>

    <h1 class="contact-name">Desmond Halvik</h1>
    <p class="licence">Lic number. 40562 .</p>

    <ul class="contact-list">
      <li>0438275160</li>
      <li>info@trupeakpower.net.au</li>
      <li>www.trupeakpower.net.au</li>
    </ul>
  </section>
</body>
</html>
```